New Website for Belcourt Manor at www.belcourt.com.au

A new logo has been designed (through pixel forge) and we now want to align the look and feel of our website at www.belcourt.com.au to the new logo. The content and page names (e.g. Grounds) will remain largely unchanged for the new site, so please submit a new look "Home" page, using our new logo, current text and any photos you choose from the existing gallery at our website. I have also attached the current "Home" page photos.

Industry/Entity Type

Accommodation

Number of Pages Required

1 page

Requirements
Must have
• Logo to be presented on white background.

```html
<!DOCTYPE html>
<html lang="en">
<head>
<meta charset="utf-8">
<title>Belcourt Manor – Home</title>
<link rel="stylesheet" href="https://fonts.googleapis.com/css2?family=Arimo:wght@400;700&family=Carlito:wght@400;700&family=Source+Sans+3:wght@700;900&display=swap">
<style>
:root{
  --blue:#2f9bd9;
  --blue-dark:#1b4f93;
  --heading-blue:#3b8fcf;
  --orange:#e8a322;
  --gold:#eebd3c;
  --text:#6a6a6a;
  --text-dark:#222;
  --rule:#c8c8c8;
  --top-strip:#f1eeea;
  --page:#f6f6f7;
  --white:#ffffff;
}
*{box-sizing:border-box;margin:0;padding:0}
html,body{width:1200px;height:1082px;overflow:hidden}
body{position:relative;background:var(--page);font-family:"Arimo",Arial,sans-serif;color:var(--text)}
a{text-decoration:none;color:inherit}
.abs{position:absolute}

/* header */
.top-strip{left:0;top:0;width:1200px;height:23px;background:var(--top-strip)}
.header{left:0;top:23px;width:1200px;height:65px;background:var(--white)}
.logo-box{left:248px;top:0;width:182px;height:88px;background:var(--white);display:flex;align-items:center;justify-content:center;gap:8px}
.logo-dot{width:14px;height:14px;border-radius:50%;background:var(--gold)}
.logo-name{font-family:"Carlito",sans-serif;font-size:24px;font-weight:400;color:var(--heading-blue);white-space:nowrap}
.tagline{left:660px;top:6px;font-size:11px;color:#555;white-space:nowrap}
.tagline b{color:var(--blue-dark)}
.top-sep{left:952px;top:5px;width:1px;height:14px;background:#ccc}
.phone{left:963px;top:5px;display:flex;align-items:center;gap:6px;font-size:12px;color:#555}
.main-nav{left:479px;top:46px;display:flex;font-family:"Carlito",sans-serif;font-weight:700;font-size:12.5px;color:var(--blue-dark);white-space:nowrap}
.main-nav a+a::before{content:"|";margin:0 6px;color:var(--blue-dark)}
.main-nav .current{color:var(--orange)}

/* hero */
.hero{left:0;top:88px;width:1200px;height:461px;background:linear-gradient(180deg,#3d5a6a 0%,#8a6a3c 28%,#c78a40 48%,#4f5550 66%,#3f8fa8 82%,#2d7f99 100%)}
.hero-band{left:0;top:445px;width:927px;height:104px;background:rgba(40,150,200,.72)}
.hero-title{left:172px;top:458px;font-family:"Source Sans 3",sans-serif;font-weight:900;font-size:41px;color:var(--white);letter-spacing:.3px;line-height:1}
.hero-sub{left:172px;top:504px;font-family:"Source Sans 3",sans-serif;font-weight:700;font-size:25px;color:var(--white);line-height:1}
.hero-arrow{top:507px;width:31px;height:31px;background:#c8962e;display:flex;align-items:center;justify-content:center}

/* content */
.col-rule{top:560px;height:1px;background:var(--rule)}
.col-div{top:560px;width:1px;height:434px;background:var(--rule)}
.notch{top:560px}
.col-title{font-family:"Carlito",sans-serif;font-size:23px;color:var(--heading-blue);font-weight:400;white-space:nowrap}
.thumb{width:227px;height:119px;background:#dcdcdc;padding:5px}
.thumb span{display:block;width:100%;height:100%;background:linear-gradient(180deg,#e9e3d8 0%,#b7a58a 55%,#7d5a3a 100%)}
.intro{width:266px;font-size:10.6px;line-height:13.6px;color:var(--text)}
.read-more{font-size:10.5px;color:var(--blue-dark)}
.read-more b{color:var(--blue)}
.grounds-list{left:781px;top:621px;width:250px;list-style:none}
.grounds-list li{height:23.5px;line-height:23px;font-family:"Carlito",sans-serif;font-size:12px;color:var(--text-dark);border-bottom:1px dotted #999;padding-left:8px;position:relative;white-space:nowrap}
.grounds-list li:last-child{border-bottom:none}
.grounds-list li::before{content:"";position:absolute;left:0;top:10px;width:4px;height:4px;background:var(--orange)}

.testimonials{left:779px;top:829px;width:272px;height:164px;background:var(--blue)}
.testimonials h3{height:30px;background:var(--gold);font-family:"Carlito",sans-serif;font-weight:400;font-size:19px;color:var(--text-dark);padding:3px 10px}
.quote{position:relative;margin:12px 12px 0 26px;font-size:11.3px;line-height:17px;color:var(--white)}
.quote::before{content:"\201C";position:absolute;left:-12px;top:-6px;font-size:22px}
.quote .end{font-size:20px;vertical-align:-6px;line-height:0}
.quote cite{display:block;text-align:right;font-style:normal;font-size:8.5px;letter-spacing:1px;line-height:12px;margin-right:8px}

/* footer */
.footer{left:0;top:1008px;width:1200px;height:74px;background:var(--blue)}
.foot-nav{left:168px;top:1020px;display:flex;font-size:11.5px;font-weight:700;color:var(--white);white-space:nowrap}
.foot-nav a+a::before{content:"|";margin:0 6px}
.foot-line{left:168px;top:1042px;width:718px;border-top:1px dotted rgba(255,255,255,.6)}
.copyright{left:177px;top:1048px;font-size:10.5px;font-weight:700;color:var(--white)}
.legal{left:182px;top:1064px;font-size:10px;color:var(--white)}
.social{left:895px;top:1029px;display:flex;gap:6px}
.social span{width:30px;height:30px;border-radius:50%;background:#1e5f9e}
</style>
</head>
<body>

<div class="abs top-strip"></div>
<div class="abs header"></div>
<div class="abs logo-box"><span class="logo-dot"></span><span class="logo-name">Belcourt Manor</span></div>
<p class="abs tagline">"We <b>GUARANTEE</b> to <b>BEAT</b> any like-for-like quotation"</p>
<div class="abs top-sep"></div>
<p class="abs phone">
  <svg width="13" height="11" viewBox="0 0 13 11"><path d="M1 3 Q6.5 -1 12 3 L11 5 L9 4 L9 3 Q6.5 2 4 3 L4 4 L2 5 Z" fill="#e8a322"/><rect x="3" y="5" width="7" height="6" rx="1" fill="#e8a322"/></svg>
  0400 123 456
</p>
<nav class="abs main-nav">
  <a class="current" href="#">HOME</a><a href="#">Mansion</a><a href="#">Bedrooms</a><a href="#">Options</a><a href="#">Wren and Otter</a><a href="#">Location</a><a href="#">Availability</a><a href="#">Gallery</a><a href="#">Contact</a>
</nav>

<div class="abs hero" role="img" aria-label="Photo of the lit mansion facade with balcony at dusk behind the saltwater pool and lounge chairs"></div>
<div class="abs hero-band"></div>
<h1 class="abs hero-title">PALATIAL ESTATE AND LUXURY RESORT</h1>
<p class="abs hero-sub">BELCOURT MANOR IS A UNIQUE GOLD COAST ESTATE.</p>
<a class="abs hero-arrow" style="left:955px" href="#" aria-label="Previous"><svg width="12" height="16"><path d="M9 2 L3 8 L9 14" stroke="#fff" stroke-width="2.2" fill="none"/></svg></a>
<a class="abs hero-arrow" style="left:993px" href="#" aria-label="Next"><svg width="12" height="16"><path d="M3 2 L9 8 L3 14" stroke="#fff" stroke-width="2.2" fill="none"/></svg></a>

<div class="abs col-rule" style="left:162px;width:884px"></div>
<div class="abs col-div" style="left:457px"></div>
<div class="abs col-div" style="left:766px;height:265px"></div>
<svg class="abs notch" style="left:172px" width="20" height="11"><path d="M0 0 H20 L10 11 Z" fill="#e8a322"/></svg>
<svg class="abs notch" style="left:466px" width="20" height="11"><path d="M0 0 H20 L10 11 Z" fill="#e8a322"/></svg>
<svg class="abs notch" style="left:777px" width="20" height="11"><path d="M0 0 H20 L10 11 Z" fill="#e8a322"/></svg>

<h2 class="abs col-title" style="left:166px;top:586px">Grand Mansion</h2>
<div class="abs thumb" style="left:164px;top:626px"><span role="img" aria-label="Photo of the mansion lounge room with leather sofas and fireplace"></span></div>
<p class="abs intro" style="left:166px;top:760px">On over 2 manicured garden acres, Belcourt Manor is a unique Gold Coast estate, centrally located in the prestigious rural suburb of Kellford. More about our Location The estate features a grand mansion, private pub (The Wren and Otter), sparkling resort pool, tennis court and playground. Magnificent properties rarely feel so warm and welcoming – so browse away and visit our photo gallery and we look forward to having you stay as our guests. For prices, availability and guest reviews, visit StayFinder. sparkling resort pool, tennis court and playground.</p>
<a class="abs read-more" style="left:358px;top:926px" href="#"><b>[+]</b>Read More</a>

<h2 class="abs col-title" style="left:476px;top:586px">The wren And otter</h2>
<div class="abs thumb" style="left:474px;top:626px"><span role="img" aria-label="Photo of the pub lounge with leather sofas and fireplace"></span></div>
<p class="abs intro" style="left:476px;top:760px">On over 2 manicured garden acres, Belcourt Manor is a unique Gold Coast estate, centrally located in the prestigious rural suburb of Kellford. More about our Location The estate features a grand mansion, private pub (The Wren and Otter), sparkling resort pool, tennis court and playground. Magnificent properties rarely feel so warm and welcoming – so browse away and visit our photo gallery and we look forward to having you stay as our guests. For prices, availability and guest reviews, visit StayFinder. sparkling resort pool, tennis court and playground.</p>
<a class="abs read-more" style="left:670px;top:926px" href="#"><b>[+]</b>Read More</a>

<h2 class="abs col-title" style="left:781px;top:586px">The Grounds</h2>
<ul class="abs grounds-list">
  <li>Security gated and fully fenced</li>
  <li>Circular driveway with off-street parking</li>
  <li>Saltwater pool with lights and solar heating</li>
  <li>Meandering pathways with lighting</li>
  <li>Town water plus 22,000 litres of tank water</li>
  <li>Circular driveway with off-street parking</li>
  <li>Saltwater pool with lights and solar heating</li>
  <li>Meandering pathways with lighting</li>
</ul>

<section class="abs testimonials">
  <h3>Testimonials</h3>
  <blockquote class="quote">It is a long established fact that a reader will be distracted by the readable. <span class="end">&#8221;</span><cite>Mira Castell</cite></blockquote>
  <blockquote class="quote" style="margin-top:10px">It is a long established fact that a reader will be distracted by the readable. <span class="end">&#8221;</span><cite>Mira Castell</cite></blockquote>
</section>

<footer class="abs footer"></footer>
<nav class="abs foot-nav">
  <a href="#">Main</a><a href="#">Mansion</a><a href="#">Bedrooms</a><a href="#">Options</a><a href="#">Wren and Otter</a><a href="#">Grounds</a><a href="#">Location</a><a href="#">Gallery</a><a href="#">Contact</a>
</nav>
<div class="abs foot-line"></div>
<p class="abs copyright">The Belcourt Manor. Copyright All Rights Reserved.</p>
<p class="abs legal">Privacy:&nbsp; Privacy | Blog | Faq's</p>
<div class="abs social"><span></span><span></span><span></span><span></span></div>

</body>
</html>
```